A wine Label for a new brand of New Zealand Wine

We are looking for a Wine Label for our "Harbor Crest" brand of wines from North Otago New Zealand. We would like the label to perhaps use the HC as a logo and the rest up to the designer. We have our vineyards located in the Waitaki Valley New Zealand which is a southern region with mountains and a river flowing past our vineyard. Photos attached of Dramatic Landscape. Also attached is a basic outline of requirements for the front bottle of the label. The rear bottle label will contain writing about the wines background plus statutory regulations on Alc. Vol, bar code etc. Front Label size to be no Larger than 80mm deep by 100 mm wide. The label can be simple or graphic, whatever the designer chooses.
Target Market(s)
New Wine Brand
Look and feel
Each slider illustrates characteristics of the customer's brand and the style your logo design should communicate.

```html
<!DOCTYPE html>
<html lang="en">
<head>
<meta charset="utf-8">
<title>Harbor Crest – Front Wine Label</title>
<link rel="stylesheet" href="https://fonts.googleapis.com/css2?family=Marcellus&family=Italianno&family=Open+Sans:wght@400;700&display=swap">
<style>
  :root {
    --page: #ffffff;
    --label-brown: #33140f;
    --cream: #ede1c6;
    --gold: #c9a24a;
    --gold-light: #e6d3a0;
  }
  * { margin: 0; padding: 0; box-sizing: border-box; }
  html, body {
    width: 1200px;
    height: 1008px;
    overflow: hidden;
    background: var(--page);
  }
  .canvas {
    position: relative;
    width: 1200px;
    height: 1008px;
  }
  .label {
    position: absolute;
    left: 182px;
    top: 162px;
    width: 836px;
    height: 815px;
    background: var(--label-brown);
    color: var(--cream);
  }
  .brand-seal {
    position: absolute;
    left: 340px;
    top: -132px;
    width: 180px;
    height: 180px;
  }
  .brand-seal svg { display: block; width: 100%; height: 100%; }
  .seal-initials {
    font-family: "Marcellus", serif;
    font-size: 64px;
    fill: var(--label-brown);
  }
  .brand-name {
    position: absolute;
    right: 89px;
    top: 180px;
    font-family: "Marcellus", serif;
    font-size: 54px;
    font-variant: small-caps;
    letter-spacing: 0.5px;
    line-height: 1;
    white-space: nowrap;
  }
  .region-line {
    position: absolute;
    left: 60px;
    top: 412px;
    transform: translate(-50%, -50%) rotate(-90deg);
    font-family: "Italianno", cursive;
    font-size: 58px;
    line-height: 1;
    white-space: nowrap;
    letter-spacing: 1px;
  }
  .wine-origin {
    position: absolute;
    left: 488px;
    top: 688px;
    font-family: "Open Sans", sans-serif;
    font-weight: 700;
    font-size: 20px;
    letter-spacing: 0.3px;
    white-space: nowrap;
  }
  .varietal {
    position: absolute;
    left: 555px;
    top: 722px;
    font-family: "Open Sans", sans-serif;
    font-weight: 400;
    font-size: 19px;
    letter-spacing: 2px;
    white-space: nowrap;
  }
</style>
</head>
<body>
  <main class="canvas">
    <section class="label" aria-label="Harbor Crest front wine label">
      <div class="brand-seal">
        <svg viewBox="0 0 180 180" aria-hidden="true">
          <circle cx="90" cy="90" r="88" fill="var(--gold-light)" stroke="var(--gold)" stroke-width="4"/>
          <text class="seal-initials" x="90" y="112" text-anchor="middle">HC</text>
        </svg>
      </div>

      <h1 class="brand-name">Harbor Crest</h1>

      <p class="region-line">2015&nbsp; Waitaki Valley North Otago</p>

      <p class="wine-origin">NEW ZEALAND WINE</p>
      <p class="varietal">pinot gris</p>
    </section>
  </main>
</body>
</html>
```